Business Cards for a law firm

Business cards for our law firm. Use our silhoette logo and OAK COUNSEL - check our website (www.oakcounsel.com)

Contact Information for Business Card

our silhouette logo, OAK COUNSEL, 800-555-0147, Dariel Montague, dariel@oakcounsel.com

Requirements
Must have
• our silhouette logo, OAK COUNSEL, 800-555-0147, Dariel Montague, dariel@oakcounsel.com

```html
<!DOCTYPE html>
<html lang="en">
<head>
<meta charset="utf-8">
<title>Oak Counsel — Business Card</title>
<link rel="stylesheet" href="https://fonts.googleapis.com/css2?family=Cinzel:wght@700&family=Barlow:wght@500&family=Libre+Bodoni:wght@400&display=swap">
<style>
  :root {
    --navy: #22346a;
    --paper: #ffffff;
    --ink-light: #ffffff;
  }
  html, body {
    margin: 0;
    padding: 0;
    overflow: hidden;
    background: var(--paper);
  }
  .card {
    position: relative;
    width: 1200px;
    height: 804px;
    background: var(--paper);
    overflow: hidden;
  }
  .brand-mark {
    position: absolute;
    left: 511px;
    top: 63px;
    width: 161px;
    height: 237px;
  }
  .firm-name {
    position: absolute;
    left: 0;
    top: 318px;
    width: 1200px;
    margin: 0;
    text-align: center;
    font-family: "Cinzel", serif;
    font-weight: 700;
    font-size: 104px;
    line-height: 1;
    letter-spacing: 0.06em;
    color: var(--navy);
  }
  .firm-tagline {
    position: absolute;
    left: 0;
    top: 449px;
    width: 1200px;
    margin: 0;
    text-align: center;
    font-family: "Barlow", sans-serif;
    font-weight: 500;
    font-size: 35px;
    line-height: 1;
    letter-spacing: 0.52em;
    text-indent: 0.52em;
    color: var(--navy);
  }
  .contact-band {
    position: absolute;
    left: 0;
    top: 537px;
    width: 1200px;
    height: 267px;
    background: var(--navy);
    color: var(--ink-light);
    font-family: "Libre Bodoni", serif;
  }
  .contact-name {
    position: absolute;
    left: 66px;
    top: 32px;
    margin: 0;
    font-weight: 400;
    font-size: 54px;
    line-height: 1;
  }
  .contact-phone,
  .contact-email {
    position: absolute;
    left: 68px;
    margin: 0;
    font-size: 24px;
    line-height: 1;
  }
  .contact-phone { top: 130px; }
  .contact-email { top: 185px; }
</style>
</head>
<body>
  <main class="card">
    <svg class="brand-mark" viewBox="0 0 161 237" role="img" aria-label="Firm silhouette logo: two standing figures in suits">
      <defs>
        <linearGradient id="markTone" x1="0" y1="0" x2="0" y2="1">
          <stop offset="0" stop-color="#2a3d76"/>
          <stop offset="1" stop-color="#22346a"/>
        </linearGradient>
      </defs>
      <rect width="161" height="237" fill="url(#markTone)"/>
    </svg>

    <h1 class="firm-name">OAK COUNSEL</h1>
    <p class="firm-tagline">INJURY ATTORNEYS</p>

    <section class="contact-band">
      <h2 class="contact-name">Dariel Montague</h2>
      <p class="contact-phone">(800) - 555 - 0147</p>
      <p class="contact-email">dariel@oakcounsel.com</p>
    </section>
  </main>
</body>
</html>
```